Stand out flyer needed for Boxing gym

Hi we need a trifold brochure designed for our outdoor boxing business it will be delivered to doctors and nutritionists to help their patients be healthier and get fit.We have supplied high res pictures for you to use in the brochure. We need a design that use a lot of yellow so it captures their attention. You can check our website for design colours www.ridgepunch.com.au

Target Market(s)

Overweight or unfit people looking to change their lives

Industry/Entity Type

Health And Wellness

Font styles to use
Sans Serif

Colors
fbee3d
ffffff
000000

Requirements
Must have
• (main heading - large bold font) Get fit lose weight & feel great
• (bold) Unlimited outdoor boxing classes $14.95
• Complete affordability & No judgements guaranteed
• (bold) Tailored programs (bold)
• Our programs are structured so that members of all fitness levels feel confident & comfortable during their start-up phase allowing you to quickly build your fitness
• (bold) Injury prevention (bold)
• Our training systems include techniques that will help you avoid injuries and build balanced strength
• (bold) Strengthen & Tone your core (bold)
• You're core muscles are some of you're most important muscles. Each workout you do incorporates core exercises to help avoid injuries and make you're total body stronger
• (bold) Wake up with more energy(bold)
• Every class you'll do will have you filled with energy the will pump you up for the rest of your day
• (bold) Sleep better(bold)
• One of the best parts of exercise is the benefit it has on your sleeping patterns. You'll sleep deeper & more sound
• (bold) Supportive environment (bold)
• At RIDGE PUNCH you'll be surrounded by trainers & other members who are there to encourage & motivate you to reach your goals and to get you moving more.
• Coupon code: SunRise27

```html
<!DOCTYPE html>
<html lang="en">
<head>
<meta charset="utf-8">
<title>Ridge Punch – Trifold Brochure</title>
<link rel="stylesheet" href="https://fonts.googleapis.com/css2?family=Fira+Sans:wght@700;800&family=Fira+Sans+Condensed:wght@300;400;600;700&display=swap">
<style>
  :root {
    --yellow: #fbee3d;
    --black: #000000;
    --charcoal: #2f2f31;
    --white: #ffffff;
    --canvas: #5d5d5d;
    --ink: #141414;
  }
  * { margin: 0; padding: 0; box-sizing: border-box; }
  html, body { width: 1200px; height: 1200px; overflow: hidden; background: var(--canvas); }
  .stage {
    position: relative; width: 1500px; height: 1500px;
    transform: scale(0.8); transform-origin: 0 0;
    font-family: "Fira Sans Condensed", "Arial Narrow", sans-serif;
  }
  .sheet { position: absolute; left: 243px; width: 1013px; height: 715px; overflow: hidden; }
  .sheet--outside { top: 26px; background: var(--charcoal); }
  .sheet--inside { top: 758px; background: var(--black); }
  .sheet svg.shapes { position: absolute; inset: 0; width: 1013px; height: 715px; }
  .text { position: absolute; }

  .heading { font-family: "Fira Sans Condensed", sans-serif; font-weight: 700; line-height: 1.02; white-space: nowrap; }
  .body { font-weight: 300; font-size: 17px; line-height: 20px; white-space: nowrap; }

  /* outside */
  .brand {
    left: 712px; top: 52px; display: flex; align-items: center; gap: 14px;
    font-family: "Fira Sans Condensed", sans-serif; font-weight: 700; font-size: 44px; color: var(--ink); letter-spacing: 1px;
  }
  .brand__mark { width: 18px; height: 18px; background: var(--ink); }
  .offer { left: 357px; top: 172px; width: 300px; text-align: center; color: var(--white); }
  .offer__lead { font-family: "Fira Sans", sans-serif; font-weight: 700; font-size: 50px; line-height: 1; }
  .offer__sub { font-weight: 600; font-size: 21px; margin-top: 2px; }
  .offer__price { font-family: "Fira Sans", sans-serif; font-weight: 800; font-size: 66px; color: var(--yellow); line-height: 1.1; }
  .offer__note { font-weight: 300; font-size: 22px; line-height: 26px; margin-top: 14px; white-space: nowrap; }
  .offer__rule { width: 52px; height: 3px; background: var(--yellow); margin: 16px auto 0; }

  .tailored { left: 35px; top: 478px; color: var(--ink); }
  .rule-dark { width: 52px; height: 3px; background: var(--ink); margin-bottom: 12px; }
  .tailored .heading { font-size: 34px; margin-bottom: 22px; }

  .contact-tag {
    left: 462px; top: 555px; font-family: "Fira Sans Condensed", sans-serif; font-weight: 700; font-size: 24px; color: var(--ink);
  }
  .contact-list { left: 372px; top: 606px; color: var(--ink); font-size: 21px; font-weight: 400; line-height: 26px; list-style: none; }
  .contact-list li { display: flex; align-items: center; gap: 10px; white-space: nowrap; }
  .contact-list svg { width: 18px; height: 18px; flex: none; }

  .headline { left: 707px; top: 496px; color: var(--white); white-space: nowrap; }
  .headline__big { font-family: "Fira Sans", sans-serif; font-weight: 800; font-size: 90px; line-height: 1; letter-spacing: -1px; }
  .headline__big span { color: var(--yellow); }
  .headline__small { font-family: "Fira Sans Condensed", sans-serif; font-weight: 700; font-size: 47px; line-height: 50px; margin-top: 6px; }

  /* inside */
  .benefit .heading { font-size: 25px; margin-bottom: 12px; }
  .injury { left: 34px; top: 124px; color: var(--ink); }
  .core { left: 34px; top: 574px; color: var(--white); }
  .core .heading { color: var(--yellow); font-size: 23px; }
  .core .body { font-size: 15px; line-height: 17.5px; }
  .energy { left: 710px; top: 30px; color: var(--white); }
  .energy .heading { color: var(--yellow); }
  .sleep { left: 372px; top: 388px; color: var(--white); }
  .sleep .heading { color: var(--yellow); }
  .sleep .body + .body { margin-top: 12px; }

  .signup { left: 810px; top: 300px; width: 165px; text-align: center; color: var(--ink); }
  .signup svg { width: 42px; height: 50px; margin: 0 auto 14px; display: block; }
  .signup .heading { font-size: 24px; }
  .signup__rule { width: 52px; height: 3px; background: var(--ink); margin: 12px auto 16px; }
  .signup__label { font-size: 15px; font-weight: 400; }
  .signup__code { font-family: "Fira Sans Condensed", sans-serif; font-weight: 700; font-size: 30px; }

  .support-title { left: 440px; top: 610px; width: 200px; text-align: right; color: var(--ink); font-size: 30px; }
  .support-divider { left: 675px; top: 615px; width: 2px; height: 65px; background: var(--ink); }
  .support-copy { left: 710px; top: 612px; color: var(--ink); font-size: 15px; line-height: 17.5px; }
</style>
</head>
<body>
<div class="stage">

  <section class="sheet sheet--outside">
    <svg class="shapes" viewBox="0 0 1013 715">
      <defs>
        <linearGradient id="trainer" x1="0" y1="0" x2="1" y2="1">
          <stop offset="0" stop-color="#2b2b2e"/><stop offset="0.5" stop-color="#3e5e8a"/><stop offset="1" stop-color="#1f5fc2"/>
        </linearGradient>
        <linearGradient id="skyline" x1="0" y1="0" x2="1" y2="1">
          <stop offset="0" stop-color="#f4f4f4"/><stop offset="1" stop-color="#cfcfcf"/>
        </linearGradient>
        <linearGradient id="boxer" x1="0" y1="0" x2="0" y2="1">
          <stop offset="0" stop-color="#4a4a4d"/><stop offset="1" stop-color="#1f1f21"/>
        </linearGradient>
        <linearGradient id="city" x1="0" y1="0" x2="0" y2="1">
          <stop offset="0" stop-color="#d8d8d8"/><stop offset="1" stop-color="#9a9a96"/>
        </linearGradient>
      </defs>
      <rect x="0" y="0" width="337" height="715" fill="url(#trainer)" role="img" aria-label="Photo: smiling trainer in blue t-shirt holding a tablet in the gym"/>
      <polygon points="0,110 190,290 190,305 0,130" fill="#fbee3d"/>
      <polygon points="0,320 337,612 337,715 0,715" fill="#fbee3d"/>
      <polygon points="445,0 1013,0 1013,490" fill="url(#skyline)" role="img" aria-label="Photo: faded city skyline with a hooded boxer"/>
      <polygon points="700,190 940,200 1013,300 1013,715 700,715" fill="url(#boxer)" role="img" aria-label="Photo: boxer in a dark hoodie with wrapped hands"/>
      <polygon points="337,395 337,715 710,715" fill="url(#city)" role="img" aria-label="Photo: city buildings and park trees"/>
      <polygon points="450,0 490,0 810,305 810,325" fill="#fbee3d"/>
      <polygon points="180,228 200,228 560,560 548,565" fill="#ffffff"/>
      <polygon points="437,548 600,548 625,592 437,592" fill="#fbee3d"/>
    </svg>

    <div class="text brand"><span class="brand__mark"></span>RIDGE PUNCH</div>

    <div class="text offer">
      <div class="offer__lead">Unlimited</div>
      <div class="offer__sub">outdoor boxing classes</div>
      <div class="offer__price">$14.95</div>
      <div class="offer__note">Complete affordability<br>&amp; No judgements guaranteed</div>
      <div class="offer__rule"></div>
    </div>

    <div class="text tailored">
      <div class="rule-dark"></div>
      <h2 class="heading">Tailored<br>programs</h2>
      <p class="body">Our programs are structured so that<br>members of all fitness levels feel<br>confident &amp; comfortable during their<br>start-up phase allowing you to quickly<br>build your fitness.</p>
    </div>

    <div class="text contact-tag">Contact Us</div>
    <ul class="text contact-list">
      <li><svg viewBox="0 0 24 24"><path d="M6.6 2l3 4.5-2 2.2a13 13 0 0 0 7.7 7.7l2.2-2 4.5 3-1.8 3.8C12 21 3 12 2.8 3.8z" fill="#141414"/></svg>0400 217 639</li>
      <li><svg viewBox="0 0 24 24"><rect x="2" y="5" width="20" height="14" fill="#141414"/><path d="M2 6l10 7 10-7" stroke="#fff" stroke-width="1.6" fill="none"/></svg>info@ridgepunch.com.au</li>
      <li><svg viewBox="0 0 24 24"><path d="M4 6h8v2H6v10h10v-6h2v8H4z M13 3h8v8l-3-3-6 6-2-2 6-6z" fill="#141414"/></svg>www.ridgepunch.com.au</li>
    </ul>

    <div class="text headline">
      <div class="headline__big">Get <span>Fit</span></div>
      <div class="headline__small">LOSE WEIGHT<br>&amp; FEEL GREAT</div>
    </div>
  </section>

  <section class="sheet sheet--inside">
    <svg class="shapes" viewBox="0 0 1013 715">
      <defs>
        <linearGradient id="stretch" x1="0" y1="0" x2="1" y2="1">
          <stop offset="0" stop-color="#c9a347"/><stop offset="0.6" stop-color="#6f7a3a"/><stop offset="1" stop-color="#2f3a22"/>
        </linearGradient>
        <linearGradient id="plank" x1="0" y1="0" x2="0" y2="1">
          <stop offset="0" stop-color="#3a3f2c"/><stop offset="0.5" stop-color="#4f6e3c"/><stop offset="1" stop-color="#7ea04a"/>
        </linearGradient>
        <linearGradient id="fighter" x1="0" y1="0" x2="0" y2="1">
          <stop offset="0" stop-color="#1a1a1a"/><stop offset="0.5" stop-color="#3a3a3a"/><stop offset="1" stop-color="#0a0a0a"/>
        </linearGradient>
        <linearGradient id="partner" x1="0" y1="0" x2="1" y2="1">
          <stop offset="0" stop-color="#f7ec4a"/><stop offset="1" stop-color="#d8d33c"/>
        </linearGradient>
      </defs>
      <polygon points="0,0 565,0 337,210 0,210" fill="url(#stretch)" role="img" aria-label="Photo: woman stretching outdoors under sunlit trees"/>
      <rect x="0" y="210" width="337" height="505" fill="url(#plank)" role="img" aria-label="Photo: man doing a plank on the grass"/>
      <polygon points="440,0 1013,0 1013,95 642,420 337,420 337,210" fill="url(#fighter)" role="img" aria-label="Photo: woman in boxing stance with wrapped fists"/>
      <polygon points="0,102 445,102 305,240 0,240" fill="rgba(251,238,61,0.82)"/>
      <polygon points="0,478 290,230 337,230 0,505" fill="#fbee3d"/>
      <polygon points="642,400 1013,80 1013,100 642,420" fill="#ffffff"/>
      <polygon points="642,432 1013,112 1013,715 355,715" fill="url(#partner)" role="img" aria-label="Photo: smiling girl clasping hands with a trainer, yellow tinted"/>
      <polygon points="315,715 642,440 642,453 330,715" fill="#fbee3d"/>
      <polygon points="360,715 642,478 642,498 385,715" fill="#ffffff"/>
      <rect x="480" y="597" width="533" height="118" fill="rgba(251,238,61,0.88)"/>
    </svg>

    <div class="text benefit injury">
      <h3 class="heading">Injury prevention</h3>
      <p class="body">Our training systems include techniques<br>that will help you avoid injuries and<br>build balanced strength.</p>
    </div>

    <div class="text benefit core">
      <h3 class="heading">Strengthen &amp; Tone your core</h3>
      <p class="body">You’re core muscles are some of you’re most<br>important muscles. Each workout you do<br>incorporates core exercises to help avoid<br>injuries and make you’re total body stronger.</p>
    </div>

    <div class="text benefit energy">
      <h3 class="heading">Wake up with more energy</h3>
      <p class="body">Every class you’ll do will have you filled<br>with energy the will pump you up for<br>the rest of your day.</p>
    </div>

    <div class="text benefit sleep">
      <h3 class="heading">Sleep better</h3>
      <p class="body">One of the best parts of exercise<br>is the benefit it has on your<br>sleeping patterns.</p>
      <p class="body">You’ll sleep deeper &amp;<br>more sound.</p>
    </div>

    <div class="text signup">
      <svg viewBox="0 0 42 50"><rect x="2" y="2" width="38" height="46" fill="none" stroke="#141414" stroke-width="4"/><rect x="11" y="14" width="20" height="3" fill="#141414"/><rect x="11" y="23" width="20" height="3" fill="#141414"/><rect x="11" y="32" width="20" height="3" fill="#141414"/></svg>
      <h3 class="heading">Sign up Today!</h3>
      <div class="signup__rule"></div>
      <div class="signup__label">COUPON CODE</div>
      <div class="signup__code">SunRise27</div>
    </div>

    <h3 class="text heading support-title">Supportive<br>environment</h3>
    <div class="text support-divider"></div>
    <p class="text body support-copy">At RIDGE PUNCH you’ll be surrounded by trainers<br>&amp; other members who are there to encourage<br>&amp; motivate you to reach your goals and to get<br>you moving more.</p>
  </section>

</div>
</body>
</html>
```